PDF flyer for our companies' two main products: Food processing machines.

PDF flyer with showcasing two products. Flyer can be one page per product, or both products on the same page.

Product #1: Labeled "Ribbon blenders".
Showing a photo of the machine, and the details/features offered with that machine. Product description must also say: "Sizes available; 2 Cu Ft. - 450 Cu Ft."

Product #2: Labeled: " Auger hoppers / Screw feeders"
Showing a photo of the machine, and the details/features offered with that machine.

SEE UPLOADED IMAGES; "Ribbon Blenders EXAMPLE FLYER".
& "Auger Hoppers / Screw Conveyors EXAMPLE FLYER" for a rough idea of what we are looking for.

Target Market(s)

Copackers, Packing houses, Food manufacturers, protein powder producers,

Industry/Entity Type

Commercial Food processing / packing / mixing equipment

Font styles to use
Serif

Colors
0054AA
0677BA
7BADD7
CADEEF
E8F1F8

Requirements
Must have
• Company logo on top of flyer.
Nice to have
• I would like for the flyer to show some stock images of common ingredients, similar to the images uploaded.
Should not have
• Pictures with background. Backgrounds must be removed from provides photos. "clipping path"

```html
<!DOCTYPE html>
<html lang="en">
<head>
<meta charset="utf-8">
<title>Keelson Equipment – Food Processing Machines</title>
<link href="https://fonts.googleapis.com/css2?family=Poppins:wght@400;500;600;700;800&display=swap" rel="stylesheet">
<style>
:root{
  --cyan:#1ba1e2;
  --ink:#111;
  --dark:#1d1b1a;
  --grey-panel:#a7a9ac;
  --stripe:#e3e4e6;
  --label:#c9cacc;
  --page:#fff;
  --backdrop:#e4e4e4;
}
*{box-sizing:border-box;margin:0;padding:0}
html,body{width:900px;height:1200px;overflow:hidden;background:var(--backdrop);font-family:'Poppins',sans-serif;color:var(--ink)}
.flyer{position:absolute;top:329px;width:420px;height:542px;background:var(--page);box-shadow:0 2px 8px rgba(0,0,0,.25);overflow:hidden}
.flyer--blender{left:20px}
.flyer--auger{left:460px}
.header{position:absolute;left:0;top:0;width:420px;height:86px}
.header svg{position:absolute;inset:0}
.brand{position:absolute;left:26px;top:33px;display:flex;align-items:center;gap:6px;color:#fff;font-weight:800;font-size:14px;letter-spacing:.5px}
.brand-dot{width:10px;height:10px;border-radius:50%;background:#fff}
.header-title{position:absolute;right:24px;top:24px;color:#fff;font-weight:800;font-size:17px;line-height:17px;text-align:right}
.product-tag{position:absolute;left:24px;background:var(--cyan);color:var(--ink);font-weight:600;font-size:11px;line-height:11px;padding:3px 6px;border-radius:4px}
.tag-rule{position:absolute;height:1.2px;background:var(--cyan)}
.sizes{position:absolute;left:25px;top:120px;font-size:8px}
.sizes-box{position:absolute;left:25px;top:131px;width:91px;height:13px;border:1.2px solid var(--ink);color:var(--cyan);font-weight:700;font-size:7px;line-height:11px;text-align:center}
.photo{position:absolute}
.features{position:absolute;border:1.2px solid var(--cyan);border-radius:8px;padding:7px 8px 6px 14px}
.features h3{font-weight:500;font-size:10.5px;line-height:12px;margin:-2px 0 5px;display:inline-block;border-bottom:1px solid var(--cyan)}
.list{list-style:none}
.list li{position:relative;font-size:5.6px;line-height:6.6px;font-weight:500;margin-bottom:4px;padding-left:9px}
.list li::before{content:"";position:absolute;left:0;top:2px;width:3.4px;height:3.4px;border-radius:50%;background:var(--ink)}
.options{position:absolute;background:var(--grey-panel);border-radius:8px;overflow:hidden}
.options h3{background:var(--cyan);font-weight:500;font-size:10.5px;text-align:center;padding:2px 0 3px;border-radius:8px 8px 0 0}
.options .list{padding:6px 10px 0 20px}
.specs{position:absolute;border-collapse:separate;border-spacing:2px 0;table-layout:fixed;font-size:4.6px;font-weight:500;text-align:center}
.specs th{background:var(--ink);color:#fff;font-weight:600;height:9px;font-size:5px}
.specs th.key{background:var(--cyan);text-align:left;padding-left:2px}
.specs td{height:7.6px;line-height:7.6px;white-space:nowrap}
.specs td.key{background:var(--label);text-align:left;padding-left:2px;font-weight:600}
.specs tr:nth-child(odd) td{background:var(--stripe)}
.specs tr:nth-child(odd) td.key{background:var(--label)}
.specs tr.spacer td{height:3px;background:none}
.url{position:absolute;left:0;right:0;top:508px;text-align:center;font-size:8.5px;font-weight:600}
.url span{color:var(--cyan)}
.url-rule{position:absolute;top:514px;height:1px;background:var(--cyan)}
.footer-band{position:absolute;left:0;bottom:0;width:420px;height:11px;background:var(--cyan)}
</style>
</head>
<body>

<!-- Ribbon blenders page -->
<section class="flyer flyer--blender">
  <header class="header">
    <svg width="420" height="86" viewBox="0 0 420 86">
      <defs>
        <linearGradient id="spiceA" x1="0" y1="0" x2="1" y2="1">
          <stop offset="0" stop-color="#4a3626"/><stop offset=".5" stop-color="#2a211b"/><stop offset="1" stop-color="#1a1715"/>
        </linearGradient>
      </defs>
      <rect x="0" y="0" width="420" height="86" fill="url(#spiceA)" role="img" aria-label="Photo of assorted spices in wooden spoons on a dark surface"/>
      <polygon points="0,0 262,0 245,86 0,86" fill="var(--cyan)"/>
    </svg>
    <div class="brand"><span class="brand-dot"></span>KEELSON</div>
    <h1 class="header-title">FOOD PROCESSING<br>MACHINES</h1>
  </header>

  <div class="product-tag" style="top:97px">RIBBON BLENDERS</div>
  <div class="tag-rule" style="left:140px;top:106px;width:230px"></div>
  <div class="sizes">Sizes available</div>
  <div class="sizes-box">2 CU FT. - 450 CU FT</div>

  <div class="photo" role="img" aria-label="Stainless steel ribbon blender on a wheeled frame with control panel" style="left:24px;top:150px;width:170px;height:175px;background:linear-gradient(160deg,#d9dadb,#8e9092 60%,#5f6163);border-radius:6px"></div>
  <div class="photo" role="img" aria-label="Four white bowls of ground spices" style="left:24px;top:342px;width:170px;height:26px;background:linear-gradient(90deg,#8a8a55,#c9b89a 30%,#b5521c 60%,#7d7a52);border-radius:12px"></div>

  <div class="features" style="left:214px;top:107px;width:180px;height:141px">
    <h3>Standard Features</h3>
    <ul class="list">
      <li>304 stainless steel construction.</li>
      <li>Pre-wired control panels with; batch timer, on/off switch, emergency stop button.</li>
      <li>Food grade compression shaft seals.</li>
      <li>Safety sensor on lid for automatic shutoff when opened.</li>
      <li>Air actuated discharge valve.</li>
      <li>1 piece hinged lid with safety grating.</li>
      <li>Power options; 220v/480v.</li>
      <li>24° standard discharge height.</li>
      <li>Castor wheels on 53cf units and smaller.</li>
    </ul>
  </div>

  <div class="options" style="left:214px;top:255px;width:180px;height:128px">
    <h3>Options</h3>
    <ul class="list">
      <li>Dual hinged lids available on custom orders.</li>
      <li>Knife gate style discharge available on custom orders.</li>
      <li>Air purge seals available on custom orders.</li>
      <li>316 stainless material available on custom orders.</li>
      <li>Custom height modification.</li>
      <li>Liquid spray systems.</li>
      <li>(VFD) Variable Frequency Drives.</li>
      <li>Leg extensions.</li>
    </ul>
  </div>

  <table class="specs" style="left:24px;top:398px;width:373px">
    <colgroup><col style="width:55px"><col span="8"></colgroup>
    <tr><th class="key">MODEL SIZE</th><th>5CF</th><th>7CF</th><th>10.5CF</th><th>17.5CF</th><th>35CF</th><th>53CF</th><th>70.5CF</th><th>106CF</th></tr>
    <tr class="spacer"><td colspan="9"></td></tr>
    <tr><td class="key">WORKING LITERS</td><td>120L</td><td>200L</td><td>300L</td><td>500L</td><td>1000L</td><td>1500L</td><td>2000L</td><td>3000L</td></tr>
    <tr><td class="key">FILL CAPACITY</td><td>5CF / 150L</td><td>9CF/250L</td><td>13CF/375L</td><td>22CF / 625L</td><td>44CF/1250L</td><td>66CF/1875L</td><td>88CF/2500L</td><td>132CF/3750L</td></tr>
    <tr><td class="key">WEIGHT</td><td>440LBS</td><td>550LBS</td><td>770LBS</td><td>1212LBS</td><td>1874LBS</td><td>2645LBS</td><td>3527LBS</td><td>5511LBS</td></tr>
    <tr><td class="key">MOTOR SIZE</td><td>4HP</td><td>5.3HP</td><td>6.7HP</td><td>10HP</td><td>14.75HP</td><td>20HP</td><td>25HP</td><td>30HP</td></tr>
    <tr><td class="key">TOTAL LENGTH</td><td>50"</td><td>53.5"</td><td>63"</td><td>72"</td><td>94"</td><td>102"</td><td>131.5"</td><td>157.5"</td></tr>
    <tr><td class="key">TOTAL WIDTH</td><td>28"</td><td>34"</td><td>41.5"</td><td>45"</td><td>52"</td><td>66"</td><td>52.5"</td><td>54"</td></tr>
    <tr><td class="key">TOTAL HEIGHT</td><td>66"</td><td>69"</td><td>71"</td><td>82"</td><td>87"</td><td>95"</td><td>78"</td><td>110"</td></tr>
    <tr><td class="key">TUB LENGTH</td><td>31.5"</td><td>35.5"</td><td>41"</td><td>47"</td><td>59"</td><td>70"</td><td>75"</td><td>100"</td></tr>
    <tr><td class="key">TUB WIDTH</td><td>16.5"</td><td>22"</td><td>25"</td><td>27.5"</td><td>35.5"</td><td>39"</td><td>48"</td><td>48"</td></tr>
    <tr><td class="key">TUB HEIGHT</td><td>20.5"</td><td>26"</td><td>28"</td><td>33"</td><td>41"</td><td>46"</td><td>51"</td><td>53"</td></tr>
    <tr><td class="key">SHAFT DIAMETER</td><td>2"</td><td>2-1/4"</td><td>2-5/8"</td><td>3"</td><td>3.5"</td><td>4"</td><td>4"</td><td>5-1/4"</td></tr>
    <tr><td class="key">TUB THICKNESS</td><td>3MM</td><td>3MM</td><td>3MM</td><td>3MM</td><td>4MM</td><td>5MM</td><td>5MM</td><td>6MM</td></tr>
    <tr><td class="key">RIBBON THICKNESS</td><td>6MM</td><td>8MM</td><td>8MM</td><td>8MM</td><td>10MM</td><td>12MM</td><td>12MM</td><td>14MM</td></tr>
    <tr><td class="key">MAX RPM</td><td>46RPM</td><td>46RPM</td><td>46RPM</td><td>46RPM</td><td>30RPM</td><td>31RPM</td><td>32RPM</td><td>33RPM</td></tr>
  </table>

  <div class="footer-band"></div>
</section>

<!-- Auger hoppers page -->
<section class="flyer flyer--auger">
  <header class="header">
    <svg width="420" height="86" viewBox="0 0 420 86">
      <defs>
        <linearGradient id="spiceB" x1="0" y1="0" x2="1" y2="1">
          <stop offset="0" stop-color="#4a3626"/><stop offset=".5" stop-color="#2a211b"/><stop offset="1" stop-color="#1a1715"/>
        </linearGradient>
      </defs>
      <rect x="0" y="0" width="420" height="86" fill="url(#spiceB)" role="img" aria-label="Photo of assorted spices in wooden spoons on a dark surface"/>
      <polygon points="0,0 262,0 245,86 0,86" fill="var(--cyan)"/>
    </svg>
    <div class="brand"><span class="brand-dot"></span>KEELSON</div>
    <h1 class="header-title">FOOD PROCESSING<br>MACHINES</h1>
  </header>

  <div class="product-tag" style="top:112px">AUGER HOPPERS /<br>SCREW CONVEYORS</div>
  <div class="tag-rule" style="left:150px;top:129px;width:236px"></div>

  <div class="photo" role="img" aria-label="Stainless steel auger hopper with inclined screw conveyor tube" style="left:8px;top:183px;width:160px;height:150px;background:linear-gradient(150deg,#eceded,#a9abad 55%,#6b6d6f);border-radius:6px"></div>

  <div class="features" style="left:210px;top:129px;width:184px;height:96px">
    <h3>Standard Features</h3>
    <ul class="list">
      <li>Direct Drive.</li>
      <li>304 Stainless steel construction.</li>
      <li>Stainless steel safety grating.</li>
      <li>Pre-wired control panel.</li>
      <li>Electric Vibrator.</li>
      <li>Castor Wheels.</li>
    </ul>
  </div>

  <div class="options" style="left:214px;top:255px;width:180px;height:97px">
    <h3>Options</h3>
    <ul class="list">
      <li>Square or round hopper. 3.5cf and 7cf hoppers are standard.</li>
      <li>Custom hoppers up to 200cf.</li>
      <li>VFD (Variable Frequency Drive).</li>
      <li>Clamshell Auger tube for easy cleanout.</li>
      <li>316 Stainless steel construction.</li>
    </ul>
  </div>

  <div class="photo" role="img" aria-label="Row of spice bowls and wooden spoons with peppercorns and ground spices" style="left:35px;top:368px;width:350px;height:34px;background:linear-gradient(90deg,#8a8a55,#c9b89a 18%,#b5521c 30%,#7d7a52 40%,#2a2422 52%,#9a9a60 64%,#b5521c 76%,#c9b89a 88%,#8a8a55);border-radius:14px"></div>

  <table class="specs" style="left:24px;top:423px;width:373px">
    <colgroup><col style="width:58px"><col span="6"></colgroup>
    <tr><th class="key">MODEL</th><th>AH-A2</th><th>AH-A3</th><th>AH-A5</th><th>AH-A7</th><th>AH-A8</th><th>AH-A12</th></tr>
    <tr class="spacer"><td colspan="7"></td></tr>
    <tr><td class="key">FEEDING RATE</td><td>2M³/HR</td><td>3M³/HR</td><td>5M³/HR</td><td>7M³/HR</td><td>8M³/HR</td><td>12M³/HR</td></tr>
    <tr><td class="key">PIPE DIAMETER</td><td>4"</td><td>4-1/2"</td><td>5-1/2"</td><td>6-1/4"</td><td>6-1/2"</td><td>8-1/2"</td></tr>
    <tr><td class="key">HOPPER VOL</td><td>3.5CF</td><td colspan="5">7CF</td></tr>
    <tr><td class="key">DIMENSIONS</td><td>28.6"x24.4"x31.5"</td><td colspan="5">40"x32"x35"</td></tr>
    <tr><td class="key">TOTAL WEIGHT</td><td>221LBS</td><td>287LBS</td><td>397LBS</td><td>441LBS</td><td>485LBS</td><td>596LBS</td></tr>
    <tr><td class="key">CHARGING HEIGHT</td><td colspan="6">STANDARD 72" (40" - 196" AVAILABLE)</td></tr>
    <tr><td class="key">CHARGING ANGLE</td><td colspan="6">STANDARD 45° (30° - 60° AVAILABLE)</td></tr>
  </table>

  <div class="url-rule" style="left:0;width:140px"></div>
  <div class="url">www.<span>keelsonequipment</span>.com</div>
  <div class="url-rule" style="left:290px;width:130px"></div>

  <div class="footer-band"></div>
</section>

</body>
</html>
```